Application for baby milk and water counter

We are building baby food app. Need to design main screen for tha app first so we can go forward to other secondary screens of the app

Food dashboard screen
Food dashboard screen is main page for view/edit food data

General vision
I see the app in pastel colors with some illustrations to make the app more in positive. You can influence from game Lantern Orchard. I see with smooth colors and gradients like in a game. Also need to have animations/transitions for each action. Each click should create smooth transition to new state. My idea is to build one dashboard screen for food which we can reuse it for other screens. So a lot of thinking should go into design stage to app appealing.

Food Dashboard
Current screen should show all the data about food intake of the baby. So here user should see

Milk How much food baby had in ml/oz. So there should be some kind of illustrated bottle or glass or smth that shows it is filled with that amount.

Add/Remove controls for food. Should be some kind of custom control for inputing amount to remove/add. I see it as a slider on the side of the bottle. User slides up or down and amount is added/removed.

Notification. So user should be aware how many hours/minutes left for next food intake. This is optional field, so consider it could be disabled. So no empty space should be on a screen. There should be human readable text. Something like. 1:30 minutes left for next intake. Maybe could be some custom made icons to illustrate that it is next food intake.

Burped: User should have ability to how much baby burped. This amount is integer value. So it could be “Baby burped 2 times today”. So again here I see some custom made/icon to illustrate how many times baby burped and amount next to it. I see changing the value just by tapping, but I don’t know how to edit if user tapped accidentally more than it should be. So TBD here.

Date and time: Dashboard should show for which date it is viewing/editing data. Should be able to change it, so user can add/edit data for yesterday. Don’t want to see here calendar on a screen so need to come up with nice design decision.

Water: User should have ability to view/edit water intake of the baby, but water is secondary information so it should be smaller than milk, or come up with some other idea how to show the water. I see to have same controls for water like for milk. Water intake is optional it can be disabled by the user.

Target Market(s)

For just became mothers

Font styles to use
Sans Serif

Colors
0094D4
00A9DD
6FCCEA
C7EBF8
E9F6FB
FFC000
F8CF3A
FAE287
FDF2CF
FEFAEE
E54698
E96AAD
F1A4CE
F9D9EA
FCEFF6

Requirements
Must have
• Ilustrations or playfull icons for show information

```html
<!DOCTYPE html>
<html lang="en">
<head>
<meta charset="utf-8">
<title>Baby Food Dashboard</title>
<link rel="stylesheet" href="https://fonts.googleapis.com/css2?family=Poppins:wght@400;500;600;700&display=swap">
<style>
  :root {
    --blue-deep: #0094D4;
    --blue: #00A9DD;
    --blue-soft: #6FCCEA;
    --blue-pale: #C7EBF8;
    --blue-mist: #E9F6FB;
    --pink-deep: #E54698;
    --pink: #E96AAD;
    --pink-soft: #F1A4CE;
    --pink-pale: #F9D9EA;
    --pink-mist: #FCEFF6;
    --yellow-pale: #FDF2CF;
    --ink: #222222;
    --white: #FFFFFF;
    --toggle-blue: #1E88E5;
  }
  * { box-sizing: border-box; margin: 0; padding: 0; }
  html, body { width: 1200px; height: 2560px; overflow: hidden; }
  body { font-family: "Poppins", sans-serif; color: var(--ink); }

  .screen {
    position: relative;
    width: 1200px;
    height: 2560px;
    overflow: hidden;
    background:
      radial-gradient(ellipse 700px 500px at 15% 35%, rgba(255,255,255,0.55), transparent 70%),
      radial-gradient(ellipse 600px 500px at 90% 55%, rgba(252,239,246,0.6), transparent 70%),
      linear-gradient(180deg, #F7C8DE 0%, #F4D3E6 25%, #EAD9EC 50%, #BFE6F0 72%, #8FDCEB 88%, #7FD6E8 100%);
  }

  .app-title {
    position: absolute;
    left: 115px;
    top: 232px;
    font-size: 78px;
    font-weight: 700;
    letter-spacing: 1px;
    line-height: 1;
  }
  .app-title .word-baby { color: var(--blue-deep); }
  .app-title .word-food { color: var(--pink-deep); }

  .hero-art {
    position: absolute;
    left: 672px;
    top: 64px;
    width: 448px;
    height: 400px;
    border-radius: 50%;
    background: radial-gradient(circle at 45% 45%, #FCE3D6 0%, #F6CFC9 55%, rgba(241,164,206,0.35) 80%, transparent 100%);
  }

  .clock {
    position: absolute;
    left: 186px;
    top: 610px;
  }
  .clock-time {
    font-size: 110px;
    font-weight: 700;
    line-height: 1;
  }
  .clock-date {
    font-size: 35px;
    font-weight: 400;
    margin-top: 20px;
  }

  .toggle {
    position: absolute;
    left: 854px;
    top: 634px;
    width: 141px;
    height: 76px;
    border-radius: 38px;
    background: var(--toggle-blue);
  }
  .toggle::after {
    content: "";
    position: absolute;
    right: 8px;
    top: 8px;
    width: 60px;
    height: 60px;
    border-radius: 50%;
    background: var(--white);
  }

  .intake-card {
    position: absolute;
    left: 160px;
    width: 883px;
    height: 352px;
    background: var(--white);
    border-radius: 26px;
    box-shadow: 0 10px 30px rgba(180, 120, 160, 0.15);
  }
  .card-milk { top: 867px; }
  .card-water { top: 1283px; }
  .card-burp { top: 1699px; }

  .card-art {
    position: absolute;
    border-radius: 40px;
  }
  .art-milk {
    left: 90px; top: 29px; width: 134px; height: 294px;
    background: linear-gradient(180deg, #E8B84A 0%, #E8B84A 12%, #E2D3DC 14%, #C9B3C2 100%);
  }
  .art-water {
    left: 32px; top: 29px; width: 250px; height: 288px;
    background: linear-gradient(180deg, #6FCCEA 0%, #C7EBF8 45%, #A9D8F0 100%);
  }
  .art-burp {
    left: 32px; top: 93px; width: 240px; height: 154px;
    background: linear-gradient(180deg, #F4C98A 0%, #E9F6FB 60%, #C7EBF8 100%);
  }

  .card-label {
    position: absolute;
    text-align: center;
  }
  .label-milk { left: 338px; top: 100px; width: 220px; }
  .label-water { left: 338px; top: 100px; width: 240px; }
  .card-label .name {
    font-size: 77px;
    font-weight: 700;
    line-height: 1.05;
  }
  .card-label .amount {
    font-size: 35px;
    font-weight: 400;
    margin-top: 6px;
  }

  .burp-text {
    position: absolute;
    left: 291px;
    top: 96px;
    font-size: 48px;
    font-weight: 600;
    line-height: 80px;
  }

  .stepper {
    position: absolute;
    left: 662px;
    top: 144px;
    display: flex;
    gap: 32px;
  }
  .stepper svg { width: 64px; height: 64px; display: block; }

  .next-intake {
    position: absolute;
    left: 157px;
    top: 2163px;
    width: 889px;
    height: 160px;
    border-radius: 80px;
    background: var(--pink-deep);
    color: var(--white);
    font-size: 48px;
    font-weight: 600;
    display: flex;
    align-items: center;
    justify-content: center;
  }
</style>
</head>
<body>
<main class="screen">
  <h1 class="app-title"><span class="word-baby">BABY</span> <span class="word-food">FOOD</span></h1>
  <div class="hero-art" role="img" aria-label="Illustration of a baby lying on a pink pillow drinking from a bottle"></div>

  <div class="clock">
    <div class="clock-time">5:20</div>
    <div class="clock-date">31-05-23</div>
  </div>
  <div class="toggle" role="switch" aria-checked="true" aria-label="Notifications"></div>

  <section class="intake-card card-milk">
    <div class="card-art art-milk" role="img" aria-label="Illustration of a milk bottle"></div>
    <div class="card-label label-milk">
      <div class="name">Milk</div>
      <div class="amount">200 ml</div>
    </div>
    <div class="stepper">
      <svg viewBox="0 0 64 64" aria-label="Add"><circle cx="32" cy="32" r="32" fill="#0094D4"/><path d="M32 18v28M18 32h28" stroke="#fff" stroke-width="5" stroke-linecap="round"/></svg>
      <svg viewBox="0 0 64 64" aria-label="Remove"><circle cx="32" cy="32" r="32" fill="#E54698"/><path d="M18 32h28" stroke="#fff" stroke-width="5" stroke-linecap="round"/></svg>
    </div>
  </section>

  <section class="intake-card card-water">
    <div class="card-art art-water" role="img" aria-label="Illustration of a cheerful blue water bottle character"></div>
    <div class="card-label label-water">
      <div class="name">Water</div>
      <div class="amount">100 ml</div>
    </div>
    <div class="stepper">
      <svg viewBox="0 0 64 64" aria-label="Add"><circle cx="32" cy="32" r="32" fill="#0094D4"/><path d="M32 18v28M18 32h28" stroke="#fff" stroke-width="5" stroke-linecap="round"/></svg>
      <svg viewBox="0 0 64 64" aria-label="Remove"><circle cx="32" cy="32" r="32" fill="#E54698"/><path d="M18 32h28" stroke="#fff" stroke-width="5" stroke-linecap="round"/></svg>
    </div>
  </section>

  <section class="intake-card card-burp">
    <div class="card-art art-burp" role="img" aria-label="Illustration of a baby sleeping on a cloud"></div>
    <p class="burp-text">Baby burped<br>2 times today</p>
    <div class="stepper">
      <svg viewBox="0 0 64 64" aria-label="Add"><circle cx="32" cy="32" r="32" fill="#0094D4"/><path d="M32 18v28M18 32h28" stroke="#fff" stroke-width="5" stroke-linecap="round"/></svg>
      <svg viewBox="0 0 64 64" aria-label="Remove"><circle cx="32" cy="32" r="32" fill="#E54698"/><path d="M18 32h28" stroke="#fff" stroke-width="5" stroke-linecap="round"/></svg>
    </div>
  </section>

  <div class="next-intake">2 hours left for next intake</div>
</main>
</body>
</html>
```